Tranvik Leasing Corp - Business Card Design

Need a new modern designed business card that is different and stands out to represent my equipment financing company. Tranvik Leasing Corp finances all types of equipment and all types of industries. We like to do equipment financing a different way by putting customers first and want our card to represent that different approach to business. I want a card that some remembers when they receive it so it sticks in their mind and makes that wow impression.

Card should have a black background so the logo stands out. It can be horizontial or vertical or a combination of both.

Front of card information is below that shows the information that would go on my card. That is where I want a different look or design to stand out. The front could be split black/orange colour so the logo could pop on black side and information on orange side with different lettering. Just outside the box thinking on the front of the card. Open to any type of design.

Back of card is below which i I like unless you have a different spin to provide or a different idea that would make the card better as I am open to anything that looks great.

Target Market(s)

Tranvik Leasing Corp deals with business owners in all industries.

Industry/Entity Type

Business

Contact Information for Business Card

Colors

Designer to choose colors to be used in the design.

Requirements
Must have
• Modern
• Different
• Stand Out
• Makes an Impression

```html
<!DOCTYPE html>
<html lang="en">
<head>
<meta charset="utf-8">
<title>Tranvik Leasing Corp – Business Card</title>
<link rel="stylesheet" href="https://fonts.googleapis.com/css2?family=Montserrat:wght@500;600;700&display=swap">
<style>
  :root {
    --stage: #2a2a2a;
    --card-black: #0b0b0b;
    --orange: #f7941d;
    --orange-deep: #f26a21;
    --red: #e8232b;
    --white: #ffffff;
    --grey: #c9c9c9;
  }
  * { box-sizing: border-box; margin: 0; padding: 0; }
  html, body {
    width: 1200px;
    height: 873px;
    overflow: hidden;
  }
  body {
    position: relative;
    background: var(--stage);
    font-family: "Montserrat", Arial, sans-serif;
  }
  .card {
    position: absolute;
    width: 560px;
    height: 320px;
    background: var(--card-black);
    border-radius: 18px;
    overflow: hidden;
    box-shadow: 0 12px 30px rgba(0,0,0,0.45);
  }

  /* Back card */
  .card--back { left: 60px; top: 90px; }
  .card--back .brand-name {
    position: absolute;
    left: 0; right: 0; top: 118px;
    display: flex;
    align-items: center;
    justify-content: center;
    gap: 12px;
  }
  .brand-dot {
    width: 18px; height: 18px;
    border-radius: 50%;
    background: var(--orange-deep);
  }
  .brand-name span {
    color: var(--orange);
    font-weight: 600;
    font-size: 26px;
    letter-spacing: 1px;
  }
  .tagline-band {
    position: absolute;
    left: 0; right: 0; bottom: 0;
    height: 44px;
    background: linear-gradient(90deg, var(--orange-deep), var(--orange));
    display: flex;
    align-items: center;
    justify-content: center;
  }
  .tagline-band p {
    color: var(--card-black);
    font-weight: 700;
    font-size: 15px;
    letter-spacing: 1.5px;
  }

  /* Front card */
  .card--front { left: 580px; top: 463px; }
  .person {
    position: absolute;
    left: 34px; top: 92px;
  }
  .person-name {
    color: var(--white);
    font-weight: 700;
    font-size: 17px;
    letter-spacing: 1.2px;
  }
  .person-title {
    color: var(--orange);
    font-weight: 600;
    font-size: 11px;
    letter-spacing: 1px;
    margin-top: 3px;
  }
  .card--front .brand-name {
    position: absolute;
    right: 30px; top: 74px;
    display: flex;
    align-items: center;
    gap: 10px;
  }
  .card--front .brand-name span { font-size: 21px; }
  .card--front .brand-dot { width: 15px; height: 15px; }
  .contact-list {
    position: absolute;
    left: 34px; top: 200px;
    list-style: none;
  }
  .contact-list li {
    display: flex;
    align-items: center;
    gap: 9px;
    color: var(--white);
    font-weight: 500;
    font-size: 13px;
    line-height: 22px;
  }
  .contact-list svg { width: 12px; height: 12px; flex: none; }
  .swoosh {
    position: absolute;
    left: 0; top: 0;
    width: 560px; height: 320px;
  }
</style>
</head>
<body>

<section class="card card--back" aria-label="Business card back">
  <div class="brand-name"><i class="brand-dot"></i><span>Tranvik Leasing Corp</span></div>
  <div class="tagline-band"><p>EQUIPMENT FINANCING EXPERTS</p></div>
</section>

<section class="card card--front" aria-label="Business card front">
  <svg class="swoosh" viewBox="0 0 560 320" aria-hidden="true">
    <path d="M0 302 C200 296 420 252 560 192 V320 H0 Z" fill="var(--orange)"/>
    <path d="M0 293 C200 287 420 240 560 166 V180 C420 252 200 293 0 297 Z" fill="var(--red)"/>
  </svg>

  <div class="person">
    <p class="person-name">MAREK OSTEN</p>
    <p class="person-title">PRESIDENT</p>
  </div>

  <div class="brand-name"><i class="brand-dot"></i><span>Tranvik Leasing Corp</span></div>

  <ul class="contact-list">
    <li>
      <svg viewBox="0 0 24 24"><path fill="var(--orange)" d="M6.6 10.8a15.1 15.1 0 0 0 6.6 6.6l2.2-2.2a1 1 0 0 1 1-.25 11.4 11.4 0 0 0 3.6.57 1 1 0 0 1 1 1V20a1 1 0 0 1-1 1A17 17 0 0 1 3 4a1 1 0 0 1 1-1h3.5a1 1 0 0 1 1 1c0 1.25.2 2.45.57 3.57a1 1 0 0 1-.25 1z"/></svg>
      403.555.0182
    </li>
    <li>
      <svg viewBox="0 0 24 24"><rect x="2" y="5" width="20" height="14" rx="1.5" fill="var(--orange)"/><path d="M3 6l9 7 9-7" fill="none" stroke="var(--card-black)" stroke-width="1.8"/></svg>
      marek@tranvikleasing.ca
    </li>
    <li>
      <svg viewBox="0 0 24 24"><circle cx="12" cy="12" r="10" fill="var(--orange)"/><path d="M2 12h20M12 2c3 3 3 17 0 20M12 2c-3 3-3 17 0 20" fill="none" stroke="var(--card-black)" stroke-width="1.4"/></svg>
      www.tranvikleasing.ca
    </li>
  </ul>
</section>

</body>
</html>
```